Rack card for a integrative medical practice

Need an eye-catching rack card with our logo with content as provided. We have a membership based holistic medical practice which incorporates western and holistic medicine. We would like to focus on wellness and healthy lifestyle. See uploaded files for what is included in the membership. Would like 2 page rack card color on both sides. Logo must be on the front.

Target Market(s)

People looking for alternative medicine, healthy lifestyle.

Industry/Entity Type

Health and Wellness

Colors
00AB8E
00BBA5
67D7C9
C6EFE9
E9F9F6

Requirements
Must have
• Must spark interest at first sight. Clear message.
Nice to have
• Warm, bright and positive vibe. Organic, neutral and earthy colors.
Should not have
• Traditional medical practice vibe (cold, formal, industrial). No PINK except the logo.

```html
<!DOCTYPE html>
<html lang="en">
<head>
<meta charset="utf-8">
<title>Sage Health &amp; Wellness — Rack Card</title>
<link href="https://fonts.googleapis.com/css2?family=DM+Serif+Display&family=Montserrat:wght@400;500;600&display=swap" rel="stylesheet">
<style>
  :root{
    --backdrop:#5e5e5e;
    --cream:#efe9dc;
    --sage:#628e75;
    --sage-text:#5e8a70;
    --forest:#0f3b2e;
    --accent:#e4418f;
    --ink:#1c1c1c;
  }
  *{margin:0;padding:0;box-sizing:border-box}
  html,body{width:1200px;height:1200px;overflow:hidden;background:var(--backdrop)}
  body{position:relative;font-family:"Montserrat",sans-serif}

  .card{position:absolute;top:135px;width:413px;height:928px;overflow:hidden}
  .card--front{left:126px;background:var(--cream)}
  .card--back{left:658px;background:var(--sage)}

  .front-art{position:absolute;left:0;top:0;width:413px;height:420px}

  .brand{position:absolute;display:flex;align-items:center;gap:8px;
    font-family:"Montserrat",sans-serif;font-weight:600;color:var(--forest);
    font-size:13px;letter-spacing:2.6px;white-space:nowrap}
  .brand__dot{width:14px;height:14px;border-radius:50%;background:var(--forest);flex:none}
  .card--front .brand{left:29px;top:500px}

  .front-title{position:absolute;left:29px;top:572px;width:375px;
    font-family:"DM Serif Display",serif;font-size:54px;line-height:65px;font-weight:400;
    color:var(--sage-text);letter-spacing:-0.5px}
  .rule{position:absolute;width:60px;height:5px;background:var(--accent)}
  .card--front .rule{left:29px;top:704px}
  .front-tagline{position:absolute;left:29px;top:722px;width:350px;
    font-size:18px;line-height:22.4px;text-transform:uppercase;color:var(--ink);font-weight:400}
  .address{position:absolute;left:29px;top:865px;display:flex;align-items:center;gap:12px;
    font-size:19px;color:var(--ink);font-weight:400;white-space:nowrap}
  .address svg{width:16px;height:20px;flex:none}
  .front-band{position:absolute;left:0;bottom:0;width:100%;height:14px;background:var(--sage)}

  .back-shape{position:absolute;left:0;top:0;width:413px;height:260px}
  .card--back .brand{left:22px;top:95px}
  .back-title{position:absolute;left:29px;top:238px;width:370px;
    font-family:"DM Serif Display",serif;font-size:33px;line-height:39px;font-weight:400;color:var(--cream)}
  .card--back .rule{left:29px;top:326px}
  .benefits{position:absolute;left:28px;top:353px;width:360px;list-style:none;
    color:var(--cream);font-size:17px;line-height:20.5px;font-weight:400}
  .benefits li{position:relative;padding-left:24px;margin-bottom:13.5px}
  .benefits li::before{content:"";position:absolute;left:2px;top:7px;width:7px;height:7px;border-radius:50%;background:var(--cream)}
  .back-band{position:absolute;left:0;bottom:0;width:100%;height:14px;background:var(--cream)}
</style>
</head>
<body>

<section class="card card--front">
  <svg class="front-art" viewBox="0 0 413 420">
    <defs>
      <radialGradient id="photoTone" cx="45%" cy="45%" r="65%">
        <stop offset="0%" stop-color="#b88468"/>
        <stop offset="55%" stop-color="#6b5448"/>
        <stop offset="100%" stop-color="#9aa59a"/>
      </radialGradient>
    </defs>
    <path d="M0 0 H188 V-7 A195 195 0 1 1 -7 188 H0 Z M0 0 V188 H188 V0 Z" fill="url(#photoTone)" role="img" aria-label="Photo of a smiling woman with eyes closed outdoors by the water"/>
    <path d="M0 0 H188 V188 H0 Z" fill="url(#photoTone)"/>
    <circle cx="188" cy="188" r="195" fill="url(#photoTone)"/>
    <circle cx="188" cy="188" r="200" fill="none" stroke="var(--sage)" stroke-width="9"/>
    <circle cx="190" cy="190" r="212" fill="none" stroke="var(--sage)" stroke-width="2.5" stroke-dasharray="180 14 60 10"/>
  </svg>

  <div class="brand"><span class="brand__dot"></span>SAGE HEALTH &amp; WELLNESS</div>

  <h1 class="front-title">Sage Health &amp; Wellness</h1>
  <div class="rule"></div>
  <p class="front-tagline">A direct primary care practice<br>focused on a more holistic<br>and personal approach to<br>medicine.</p>

  <div class="address">
    <svg viewBox="0 0 16 20"><path d="M8 0C3.6 0 0 3.4 0 7.7 0 13 8 20 8 20s8-7 8-12.3C16 3.4 12.4 0 8 0zm0 10.5a3 3 0 1 1 0-6 3 3 0 0 1 0 6z" fill="var(--sage)"/></svg>
    <span>1472 Birch Ave., STE 2B Fairview</span>
  </div>
  <div class="front-band"></div>
</section>

<section class="card card--back">
  <svg class="back-shape" viewBox="0 0 413 260">
    <circle cx="125" cy="-25" r="232" fill="var(--cream)"/>
  </svg>

  <div class="brand"><span class="brand__dot"></span>SAGE HEALTH &amp; WELLNESS</div>

  <h2 class="back-title">What’s Included in Your Membership :</h2>
  <div class="rule"></div>
  <ul class="benefits">
    <li>Unlimited office visits with no copay</li>
    <li>Direct communication with your<br>doctor</li>
    <li>Discounted labs, imaging and<br>medications</li>
    <li>Free initial acupuncture session ($250<br>value).</li>
    <li>2 CoreScan testings per year ($100 value)</li>
    <li>Discounts for supplements and health<br>products in the clinic</li>
    <li>Discounts for iv vitamin infusion<br>therapy</li>
    <li>Personalized nutrition plan after<br>advanced testing such as gut<br>microbiome, hormonal, metabo-<br>lism test, etc.</li>
  </ul>
  <div class="back-band"></div>
</section>

</body>
</html>
```